Graphic Design Set for Banner Ads - Sizes and Specs for Bidlane

We need a set of 6 ads of the following sizes created for Bidlane:

Medium rectangle: 300×250
Leaderboard: 728×90
Wide skyscraper: 160×600
Large rectangle: 300x600
Mobile leaderboard: 320×50

Here are the Formatting Guidelines (WEB ADS): https://help.bidlane.com/hc/en-us/articles/583920147-Ad-Content-and-Format-Guidelines

Here is the website: https://mavenhollowcare.com/

Here are some words for the ad - feel free to use creative liberties if you have something better or need less words.

1. The Future of Aging is Here

2. Dementia At-Home Care

3. Benefits of an Assisted Living from the Privacy of Your Home - link to

4. Idaho's New Senior Care Option

5. The Security of Senior Living from the Comfort of Your Home

I have the images for all website photos, if you need more images, please let me know.

Target Market(s)

Women age 55+

Industry/Entity Type

Graphic Design

Requirements
Must have
• Incorporate website imagery as much as possible
Should not have
• a feeling of helplessness, old, etc.

```html
<!DOCTYPE html>
<html lang="en">
<head>
<meta charset="utf-8">
<title>Maven Hollow — Banner Ad Set for Bidlane</title>
<link href="https://fonts.googleapis.com/css2?family=Roboto+Slab:wght@300;400&family=Montserrat:wght@600;700&display=swap" rel="stylesheet">
<style>
:root{
  --page:#ffffff;
  --ink:#3a3a3a;
  --white:#ffffff;
  --aging-red:#e0393e;
  --dementia-blue:#3d86ad;
  --benefit-blue:#2c56a8;
  --option-yellow:#e8df1e;
  --option-olive:#b7a229;
  --security-yellow:#e6d65a;
  --teal-dark:#2a8a80;
  --teal:#3a9c8f;
  --stone:#c9cabd;
  --mist:#e1e1e1;
  --peach:#d9a889;
}
*{margin:0;padding:0;box-sizing:border-box}
html,body{width:1200px;height:1171px;overflow:hidden;background:var(--page)}
.board{position:relative;width:1200px;height:1171px}
.ad{position:absolute;overflow:hidden}
.photo{position:absolute}
.t{position:absolute;white-space:nowrap;line-height:1}
.slab{font-family:"Roboto Slab",Georgia,serif;font-weight:300}
.caps{font-family:"Montserrat",Arial,sans-serif;font-weight:600;letter-spacing:.12em;text-transform:uppercase}
.brand{position:absolute;white-space:nowrap;line-height:1;font-family:"Roboto Slab",Georgia,serif;font-weight:300;font-size:11px}
.brand-dark{color:var(--ink)}
.brand-light{color:var(--white)}
.red{color:var(--aging-red)}
.blue{color:var(--dementia-blue)}
.navy{color:var(--benefit-blue)}
.white{color:var(--white)}
.ink{color:var(--ink)}
.grey{color:#666}
.yellow{color:var(--security-yellow)}
.option{color:var(--option-yellow)}
.olive{color:var(--option-olive)}

/* photo areas: soft fills in the photo's main tones */
.ph-yoga{background:linear-gradient(180deg,#85846c 0%,#a9978f 100%)}
.ph-yoga-h{background:linear-gradient(90deg,#7f7d68 0%,#64654b 100%)}
.ph-garden{background:linear-gradient(180deg,#7c6c70 0%,#9d8a80 100%)}
.ph-garden-fade{background:linear-gradient(180deg,var(--mist) 0%,#8e8474 35%,#9c8780 100%)}
.ph-garden-h{background:linear-gradient(90deg,rgba(160,130,110,0) 0%,#8d7d6e 40%,#a3918a 100%)}
.ph-man{background:linear-gradient(180deg,#b6a08e 0%,#3b3634 100%)}
.ph-man-teal{background:linear-gradient(180deg,rgba(42,138,128,0) 0%,#2a6c66 60%,#1f524e 100%)}
</style>
</head>
<body>
<main class="board">

<!-- ===== Set 1: The future of aging ===== -->
<section class="ad" style="left:25.6px;top:25.6px;width:152px;height:126.4px">
  <div class="photo ph-yoga" style="inset:0" role="img" aria-label="Woman doing a yoga pose on a mat by a lake"></div>
  <span class="brand brand-light" style="left:9px;top:8px">Maven Hollow</span>
  <span class="t caps white" style="left:10px;top:63px;font-size:8px">The</span>
  <span class="t slab white" style="left:10px;top:72px;font-size:18px">future of aging</span>
  <span class="t caps white" style="right:12px;top:104px;font-size:8px">Is here</span>
</section>

<section class="ad" style="left:25.6px;top:162.4px;width:152px;height:304px;background:var(--stone)">
  <div class="photo ph-yoga" style="left:0;right:0;top:150px;bottom:0" role="img" aria-label="Woman doing a yoga pose on a mat by a lake"></div>
  <span class="brand brand-dark" style="left:10px;top:10px;font-size:13px">Maven Hollow</span>
  <span class="t caps white" style="left:10px;top:99px;font-size:8px">The</span>
  <span class="t slab red" style="left:10px;top:108px;font-size:19px">future of aging</span>
  <span class="t caps white" style="right:11px;top:131px;font-size:8px">Is here</span>
</section>

<section class="ad" style="left:188px;top:162.4px;width:81.6px;height:304px;background:var(--stone)">
  <div class="photo ph-yoga" style="left:0;right:0;top:170px;bottom:0" role="img" aria-label="Woman doing a yoga pose on a mat by a lake"></div>
  <span class="brand brand-dark" style="left:8px;top:10px;font-size:10px">Maven Hollow</span>
  <span class="t caps white" style="left:10px;top:58px;font-size:8px">The</span>
  <span class="t slab red" style="left:10px;top:70px;font-size:19px">future</span>
  <span class="t slab red" style="left:10px;top:91px;font-size:19px">of</span>
  <span class="t slab red" style="left:10px;top:110px;font-size:19px">aging</span>
  <span class="t caps white" style="left:11px;top:135px;font-size:8px">Is here</span>
</section>

<section class="ad" style="left:25.6px;top:477.6px;width:369.6px;height:57.6px">
  <div class="photo ph-yoga-h" style="inset:0" role="img" aria-label="Woman doing a yoga pose on a mat by a lake"></div>
  <span class="t caps white" style="left:87px;top:6px;font-size:9px">The</span>
  <span class="t slab white" style="left:87px;top:16px;font-size:20px">future of aging</span>
  <span class="t caps white" style="left:88px;top:41px;font-size:8px">Is here</span>
  <span class="brand brand-light" style="right:12px;top:23px;font-size:12px">Maven Hollow</span>
</section>

<section class="ad" style="left:25.6px;top:545.6px;width:162.4px;height:24px">
  <div class="photo ph-yoga-h" style="inset:0" role="img" aria-label="Woman doing a yoga pose on a mat by a lake"></div>
  <span class="t caps white" style="left:24px;top:9px;font-size:5px">The</span>
  <span class="t slab white" style="left:39px;top:4px;font-size:10px">future of aging</span>
  <span class="t caps white" style="left:98px;top:17px;font-size:4.5px">Is here</span>
  <span class="brand brand-light" style="right:4px;top:9px;font-size:5.5px">Maven Hollow</span>
</section>

<!-- ===== Set 2: Dementia at-home care ===== -->
<section class="ad" style="left:415.2px;top:25.6px;width:152px;height:126.4px">
  <div class="photo ph-garden" style="inset:0" role="img" aria-label="Smiling older woman in a garden chair beside a curly white dog"></div>
  <span class="brand brand-light" style="right:6px;top:8px">Maven Hollow</span>
  <span class="t slab white" style="left:7px;top:87px;font-size:19px">Dementia</span>
  <span class="t caps white" style="left:98px;top:93px;font-size:7px">At-home</span>
  <span class="t caps white" style="left:98px;top:103px;font-size:7px">care</span>
</section>

<section class="ad" style="left:415.2px;top:162.4px;width:152px;height:304px;background:var(--mist)">
  <div class="photo ph-garden-fade" style="left:0;right:0;top:95px;bottom:0" role="img" aria-label="Smiling older woman in a garden chair beside a curly white dog"></div>
  <span class="brand brand-dark" style="right:10px;top:10px;font-size:13px">Maven Hollow</span>
  <span class="t slab blue" style="left:7px;top:60px;font-size:30px">Dementia</span>
  <span class="t caps white" style="left:7px;top:267px;font-size:8px">At-home</span>
  <span class="t caps white" style="left:7px;top:278px;font-size:8px">care</span>
</section>

<section class="ad" style="left:577.6px;top:162.4px;width:81.6px;height:304px;background:var(--mist)">
  <div class="photo ph-garden-fade" style="left:0;right:0;top:150px;bottom:0" role="img" aria-label="Smiling older woman in a garden chair beside a curly white dog"></div>
  <span class="brand brand-dark" style="left:6px;top:10px;font-size:10px">Maven Hollow</span>
  <span class="t slab blue" style="left:6px;top:62px;font-size:15px">Dementia</span>
  <span class="t caps grey" style="left:8px;top:81px;font-size:6.5px">At-home</span>
  <span class="t caps grey" style="left:8px;top:91px;font-size:6.5px">care</span>
</section>

<section class="ad" style="left:415.2px;top:477.6px;width:369.6px;height:57.6px;background:linear-gradient(90deg,#ffffff 0%,#f2e1d6 30%,var(--peach) 55%)">
  <div class="photo ph-garden-h" style="left:150px;right:0;top:0;bottom:0" role="img" aria-label="Smiling older woman in a garden chair beside a curly white dog"></div>
  <span class="t slab blue" style="left:13px;top:4px;font-size:28px">Dementia</span>
  <span class="t caps ink" style="left:14px;top:37px;font-size:7px">At-home care</span>
  <span class="brand brand-light" style="right:8px;top:8px;font-size:12px">Maven Hollow</span>
</section>

<section class="ad" style="left:415.2px;top:545.6px;width:162.4px;height:24px;background:var(--peach)">
  <div class="photo ph-garden-h" style="left:80px;right:0;top:0;bottom:0" role="img" aria-label="Smiling older woman in a garden chair beside a curly white dog"></div>
  <span class="t caps white" style="left:28px;top:2px;font-size:5px">At-home care</span>
  <span class="t slab white" style="left:6px;top:8px;font-size:14px">Dementia</span>
  <span class="brand brand-light" style="right:5px;top:9px;font-size:5.5px">Maven Hollow</span>
</section>

<!-- ===== Set 3: Benefits of assisted living at home ===== -->
<section class="ad" style="left:804.8px;top:25.6px;width:152px;height:126.4px;background:linear-gradient(90deg,#c6c7a8,#d8e8d2)">
  <div class="photo ph-man" style="left:0;top:0;width:78px;bottom:0" role="img" aria-label="Portrait of a smiling older man with a white moustache"></div>
  <span class="t caps navy" style="left:84px;top:7px;font-size:7px">The</span>
  <span class="t caps navy" style="left:84px;top:18px;font-size:7px">Benefits</span>
  <span class="t caps navy" style="left:84px;top:29px;font-size:7px">of</span>
  <span class="t caps navy" style="left:84px;top:40px;font-size:7px">Assisted</span>
  <span class="t caps navy" style="left:84px;top:51px;font-size:7px">Living</span>
  <span class="t slab ink" style="left:128px;top:54px;font-size:15px">at</span>
  <span class="t slab ink" style="left:84px;top:68px;font-size:21px">home</span>
  <span class="brand brand-light" style="left:4px;top:108px;font-size:10px">Maven Hollow</span>
</section>

<section class="ad" style="left:804.8px;top:162.4px;width:152px;height:304px;background:linear-gradient(180deg,#cfd0ae 0%,#b9dcc0 60%,#8ac8a6 100%)">
  <div class="photo ph-man" style="left:0;right:0;top:135px;bottom:0" role="img" aria-label="Portrait of a smiling older man with a white moustache"></div>
  <span class="brand brand-dark" style="left:15px;top:20px;font-size:13px">Maven Hollow</span>
  <span class="t caps navy" style="left:17px;top:81px;font-size:7.5px">The benefits of</span>
  <span class="t caps navy" style="left:17px;top:93px;font-size:9px">Assisted living</span>
  <span class="t slab ink" style="left:15px;top:106px;font-size:29px">at home</span>
</section>

<section class="ad" style="left:967.2px;top:162.4px;width:81.6px;height:304px;background:linear-gradient(180deg,#cfd2b3 0%,#b8dcc4 70%,#a9d3bb 100%)">
  <div class="photo ph-man" style="left:0;right:0;top:190px;bottom:0" role="img" aria-label="Portrait of a smiling older man with a white moustache"></div>
  <span class="brand brand-dark" style="left:6px;top:12px;font-size:10px">Maven Hollow</span>
  <span class="t caps navy" style="left:8px;top:41px;font-size:8px">The</span>
  <span class="t caps navy" style="left:8px;top:54px;font-size:8px">Benefits</span>
  <span class="t caps navy" style="left:8px;top:67px;font-size:8px">of</span>
  <span class="t caps navy" style="left:8px;top:80px;font-size:8px">Assisted</span>
  <span class="t caps navy" style="left:8px;top:93px;font-size:8px">Living</span>
  <span class="t slab ink" style="left:7px;top:107px;font-size:25px">at</span>
  <span class="t slab ink" style="left:7px;top:135px;font-size:25px">home</span>
</section>

<section class="ad" style="left:804.8px;top:477.6px;width:369.6px;height:57.6px;background:linear-gradient(90deg,#c6c9a8 0%,#cfe3cf 40%,#d9ecd4 100%)">
  <div class="photo ph-man" style="left:0;top:0;width:90px;bottom:0" role="img" aria-label="Portrait of a smiling older man with a white moustache"></div>
  <span class="t caps navy" style="left:99px;top:14px;font-size:7.5px">The benefits of assisted living</span>
  <span class="t slab grey" style="left:98px;top:24px;font-size:22px">at home</span>
  <span class="brand brand-dark" style="right:8px;top:26px;font-size:12px">Maven Hollow</span>
</section>

<section class="ad" style="left:804.8px;top:545.6px;width:162.4px;height:24px;background:linear-gradient(90deg,#c6c9a8,#d9ecd4)">
  <div class="photo ph-man" style="left:0;top:0;width:40px;bottom:0" role="img" aria-label="Portrait of a smiling older man with a white moustache"></div>
  <span class="t caps navy" style="left:43px;top:4px;font-size:4.5px">The benefits of assisted living</span>
  <span class="t slab ink" style="left:42px;top:11px;font-size:11px">at home</span>
  <span class="brand brand-dark" style="right:6px;top:13px;font-size:5.5px">Maven Hollow</span>
</section>

<!-- ===== Set 4: Idaho's new senior care option ===== -->
<section class="ad" style="left:25.6px;top:600.8px;width:152px;height:126.4px">
  <div class="photo ph-garden" style="inset:0" role="img" aria-label="Smiling older woman in a garden chair beside a curly white dog"></div>
  <span class="brand brand-light" style="right:6px;top:6px">Maven Hollow</span>
  <span class="t caps white" style="left:6px;top:71px;font-size:9px;font-weight:700">Idaho's new</span>
  <span class="t slab white" style="left:5px;top:80px;font-size:25px">Senior Care</span>
  <span class="t slab option" style="left:5px;top:104px;font-size:17px">Option</span>
</section>

<section class="ad" style="left:25.6px;top:737.6px;width:152px;height:304px;background:var(--mist)">
  <div class="photo ph-garden-fade" style="left:0;right:0;top:110px;bottom:0" role="img" aria-label="Smiling older woman in a garden chair beside a curly white dog"></div>
  <span class="brand brand-dark" style="left:5px;top:7px;font-size:13px">Maven Hollow</span>
  <span class="t caps ink" style="left:6px;top:66px;font-size:9px;font-weight:700">Idaho's new</span>
  <span class="t slab ink" style="left:5px;top:74px;font-size:26px">Senior Care</span>
  <span class="t slab option" style="left:96px;top:100px;font-size:13px;font-weight:400">Option</span>
</section>

<section class="ad" style="left:188px;top:737.6px;width:81.6px;height:304px;background:var(--mist)">
  <div class="photo ph-garden-fade" style="left:0;right:0;top:165px;bottom:0" role="img" aria-label="Smiling older woman in a garden chair beside a curly white dog"></div>
  <span class="brand brand-dark" style="left:6px;top:12px;font-size:10px">Maven Hollow</span>
  <span class="t caps ink" style="left:6px;top:67px;font-size:6.5px;font-weight:700">Idaho's new</span>
  <span class="t slab ink" style="left:5px;top:75px;font-size:21px">Senior</span>
  <span class="t slab ink" style="left:5px;top:97px;font-size:21px">Care</span>
  <span class="t slab olive" style="left:5px;top:120px;font-size:17px;font-weight:400">Option</span>
</section>

<section class="ad" style="left:25.6px;top:1052px;width:369.6px;height:57.6px;background:linear-gradient(90deg,#c9906c 0%,var(--peach) 40%,#e2c8b7 60%)">
  <div class="photo ph-garden-h" style="left:170px;right:0;top:0;bottom:0" role="img" aria-label="Smiling older woman in a garden chair beside a curly white dog"></div>
  <span class="t caps white" style="left:18px;top:15px;font-size:8.5px;font-weight:700">Idaho's new</span>
  <span class="t slab option" style="left:38px;top:25px;font-size:17px">Senior Care <span class="white">Option</span></span>
  <span class="brand brand-light" style="right:8px;top:10px;font-size:12px">Maven Hollow</span>
</section>

<section class="ad" style="left:25.6px;top:1120px;width:162.4px;height:24px;background:linear-gradient(90deg,#c9906c,var(--peach))">
  <div class="photo ph-garden-h" style="left:80px;right:0;top:0;bottom:0" role="img" aria-label="Smiling older woman in a garden chair beside a curly white dog"></div>
  <span class="t caps white" style="left:6px;top:3px;font-size:5px;font-weight:700">Idaho's new</span>
  <span class="t slab option" style="left:5px;top:10px;font-size:10px">Senior Care <span class="white">Option</span></span>
  <span class="brand brand-light" style="right:5px;top:5px;font-size:5.5px">Maven Hollow</span>
</section>

<!-- ===== Set 5: Security & comfort ===== -->
<section class="ad" style="left:415.2px;top:600.8px;width:152px;height:126.4px;background:var(--teal-dark)">
  <div class="photo ph-man-teal" style="left:70px;right:0;top:0;bottom:0" role="img" aria-label="Portrait of an older man, tinted teal"></div>
  <span class="brand brand-light" style="left:6px;top:6px;font-size:10px">Maven Hollow</span>
  <span class="t caps white" style="left:6px;top:41px;font-size:8.5px;font-weight:700">The</span>
  <span class="t slab yellow" style="left:6px;top:47px;font-size:19px">security</span>
  <span class="t caps white" style="left:6px;top:70px;font-size:6.5px">Of assisted living</span>
  <span class="t caps white" style="left:6px;top:82px;font-size:8.5px;font-weight:700">The</span>
  <span class="t slab yellow" style="left:6px;top:88px;font-size:19px">comfort</span>
  <span class="t caps white" style="left:6px;top:109px;font-size:6.5px">Of independent living</span>
</section>

<section class="ad" style="left:415.2px;top:737.6px;width:152px;height:304px;background:linear-gradient(180deg,var(--teal-dark) 0%,var(--teal) 60%,#2f6f6a 100%)">
  <div class="photo ph-man-teal" style="left:0;right:0;top:130px;bottom:0" role="img" aria-label="Portrait of an older man, tinted teal"></div>
  <span class="brand brand-light" style="right:6px;top:10px;font-size:12px">Maven Hollow</span>
  <span class="t caps white" style="left:10px;top:35px;font-size:9px;font-weight:700">The</span>
  <span class="t slab yellow" style="left:10px;top:42px;font-size:22px">security</span>
  <span class="t caps white" style="left:10px;top:69px;font-size:7px">Of assisted living</span>
  <span class="t caps white" style="left:10px;top:88px;font-size:9px;font-weight:700">The</span>
  <span class="t slab yellow" style="left:10px;top:95px;font-size:22px">comfort</span>
  <span class="t caps white" style="left:10px;top:120px;font-size:7px">Of independent living</span>
</section>

<section class="ad" style="left:577.6px;top:737.6px;width:81.6px;height:304px;background:linear-gradient(180deg,var(--teal-dark),var(--teal))">
  <div class="photo ph-man-teal" style="left:0;right:0;top:180px;bottom:0" role="img" aria-label="Portrait of an older man, tinted teal"></div>
  <span class="brand brand-light" style="right:4px;top:10px;font-size:10px">Maven Hollow</span>
  <span class="t caps white" style="left:4px;top:50px;font-size:8.5px;font-weight:700">The</span>
  <span class="t slab yellow" style="left:4px;top:57px;font-size:17px">security</span>
  <span class="t caps white" style="left:4px;top:77px;font-size:7px">Of</span>
  <span class="t caps white" style="left:4px;top:88px;font-size:7px">Assisted</span>
  <span class="t caps white" style="left:4px;top:99px;font-size:7px">Living</span>
  <span class="t caps white" style="left:4px;top:117px;font-size:8.5px;font-weight:700">The</span>
  <span class="t slab yellow" style="left:4px;top:124px;font-size:17px">comfort</span>
  <span class="t caps white" style="left:4px;top:144px;font-size:7px">Of</span>
  <span class="t caps white" style="left:4px;top:155px;font-size:7px">Independent</span>
  <span class="t caps white" style="left:4px;top:166px;font-size:7px">Living</span>
</section>

<section class="ad" style="left:415.2px;top:1052px;width:369.6px;height:57.6px;background:linear-gradient(90deg,#3cc296 0%,#33a58e 45%,#2c8a82 100%)">
  <div class="photo ph-man-teal" style="left:300px;right:0;top:0;bottom:0;opacity:.6" role="img" aria-label="Portrait of an older man, tinted teal"></div>
  <span class="brand brand-light" style="left:13px;top:24px;font-size:10px">Maven Hollow</span>
  <span class="t caps white" style="left:95px;top:12px;font-size:9px;font-weight:700">The</span>
  <span class="t slab yellow" style="left:95px;top:19px;font-size:22px">security</span>
  <span class="t caps white" style="left:95px;top:44px;font-size:7px">Of assisted living</span>
  <span class="t caps white" style="left:221px;top:12px;font-size:9px;font-weight:700">The</span>
  <span class="t slab yellow" style="left:221px;top:19px;font-size:22px">comfort</span>
  <span class="t caps white" style="left:221px;top:44px;font-size:7px">Of independent living</span>
</section>

<section class="ad" style="left:415.2px;top:1120px;width:162.4px;height:24px;background:linear-gradient(90deg,#3cc296,#2c8a82)">
  <span class="brand brand-light" style="left:5px;top:9px;font-size:5.5px">Maven Hollow</span>
  <span class="t caps white" style="left:52px;top:2px;font-size:4.5px;font-weight:700">The</span>
  <span class="t slab yellow" style="left:52px;top:6px;font-size:10px">security</span>
  <span class="t caps white" style="left:52px;top:17px;font-size:3.5px">Of assisted living</span>
  <span class="t caps white" style="left:104px;top:2px;font-size:4.5px;font-weight:700">The</span>
  <span class="t slab yellow" style="left:104px;top:6px;font-size:10px">comfort</span>
  <span class="t caps white" style="left:104px;top:17px;font-size:3.5px">Of independent living</span>
</section>

</main>
</body>
</html>
```